It is an assisted living facility. I wanted the name to reflect that we are a step above other facilities; i.e., professionally decorated rooms, cloth napkins, family dinners, etc. My motto is: COME WHERE YOU ARE CELEBRATED! Also, I have thought about having a house held with the "Hands" and the motto around it but I have seen that logo used other places. In other words, HELP!

I do not have a photo yet, but the photographer is coming next week. I would like the back of the card to have a picture of the facility.

BRIGHT MEADOW ASSISTED LIVING, LLC, 2386 Pennwick Dr., FL 33471-2830
Phone: (813) 555-0148; Fax: (813)
Doris Pelling, Owner/Administrator

```html
<!DOCTYPE html>
<html lang="en">
<head>
<meta charset="utf-8">
<title>Bright Meadow Assisted Living – Business Cards</title>
<link rel="stylesheet" href="https://fonts.googleapis.com/css2?family=Oswald:wght@700&family=Arimo:wght@400;700&display=swap">
<style>
  :root {
    --page: #ebebeb;
    --green: #56ab0a;
    --green-light: #a6d65a;
    --dark: #2b2a29;
    --orange: #ff6a00;
    --amber: #f7941d;
    --yellow: #ffcc00;
    --white: #ffffff;
    --logo-green: #8cc63f;
  }
  * { margin: 0; padding: 0; box-sizing: border-box; }
  html, body { width: 888px; height: 1200px; overflow: hidden; }
  body {
    background: var(--page);
    font-family: "Arimo", Arial, sans-serif;
    position: relative;
  }
  .card {
    position: absolute;
    overflow: hidden;
    background: var(--green);
    box-shadow: 0 6px 14px rgba(0,0,0,0.28);
  }
  .card-rounded { left: 60px; top: 152px; width: 748px; height: 431px; border-radius: 44px; }
  .card-square  { left: 77px; top: 685px; width: 720px; height: 435px; }
  .card-bg { position: absolute; inset: 0; width: 100%; height: 100%; }
  .motto {
    position: absolute;
    left: 0; right: 0;
    text-align: center;
    font-family: "Oswald", "Arial Narrow", sans-serif;
    font-weight: 700;
    font-size: 44px;
    letter-spacing: -0.5px;
    color: var(--white);
    -webkit-text-stroke: 2px #222;
    paint-order: stroke fill;
    transform: scaleX(0.86);
    line-height: 1;
  }
  .card-rounded .motto { top: 62px; }
  .card-square .motto { top: 34px; }
  .contact { position: absolute; color: var(--white); }
  .contact .name { font-weight: 700; font-size: 23px; line-height: 1; }
  .contact .role { font-size: 20px; margin-top: 6px; line-height: 1; }
  .contact ul { list-style: none; margin-top: 28px; }
  .contact li {
    display: flex; align-items: center; gap: 6px;
    font-size: 17.5px; height: 24px; margin-bottom: 14px;
  }
  .contact-right { right: 64px; top: 196px; text-align: right; }
  .contact-right li { justify-content: flex-end; }
  .contact-left { left: 55px; top: 166px; }
  .contact-left ul { margin-top: 40px; }
  .contact-left li { margin-bottom: 18px; gap: 10px; }
  .icon { width: 22px; height: 24px; flex: none; }
  .brand {
    position: absolute;
    font-family: "Arimo", Arial, sans-serif;
    font-weight: 700;
    color: var(--logo-green);
    font-size: 19px;
    line-height: 1.3;
    text-align: center;
  }
  .card-rounded .brand { left: 48px; top: 322px; width: 200px; }
  .card-square .brand { left: 450px; top: 330px; width: 200px; }
</style>
</head>
<body>

<svg width="0" height="0" style="position:absolute">
  <defs>
    <linearGradient id="stripe" x1="0" x2="1" y1="0" y2="0">
      <stop offset="0" stop-color="#ff6a00"/>
      <stop offset="1" stop-color="#ffcc00"/>
    </linearGradient>
    <symbol id="icon-phone" viewBox="0 0 22 24">
      <path d="M5 2 L9 2 L10 7 L7.5 9 C8.5 12 10.5 15 13.5 17 L15.5 14.5 L20 16 L20 20 C20 21.5 18.5 22.5 17 22 C9.5 20 3.5 13 2.5 5 C2.3 3.3 3.4 2 5 2 Z" fill="#f7941d"/>
    </symbol>
    <symbol id="icon-fax" viewBox="0 0 22 24">
      <rect x="5" y="3" width="12" height="8" fill="none" stroke="#f7941d" stroke-width="2"/>
      <rect x="1" y="10" width="20" height="11" rx="1.5" fill="#f7941d"/>
      <rect x="5" y="14" width="12" height="2" fill="#2b2a29"/>
      <rect x="5" y="17.5" width="12" height="1.5" fill="#2b2a29"/>
    </symbol>
    <symbol id="icon-pin" viewBox="0 0 22 24">
      <path d="M11 1 C6 1 3 4.5 3 9 C3 14 11 23 11 23 C11 23 19 14 19 9 C19 4.5 16 1 11 1 Z" fill="#f7941d"/>
      <circle cx="11" cy="9" r="3.2" fill="#2b2a29"/>
    </symbol>
  </defs>
</svg>

<section class="card card-rounded">
  <svg class="card-bg" viewBox="0 0 748 431" preserveAspectRatio="none">
    <path d="M0 150 C250 128 500 170 748 152 L748 431 L0 431 Z" fill="var(--dark)"/>
    <path d="M0 150 C250 128 500 170 748 152" fill="none" stroke="url(#stripe)" stroke-width="8"/>
  </svg>
  <h1 class="motto">COME WHERE YOU ARE CELEBRATED!</h1>
  <p class="brand">BRIGHT MEADOW<br>ASSISTED LIVING</p>
  <div class="contact contact-right">
    <p class="name">Doris Pelling</p>
    <p class="role">Owner/Administrator</p>
    <ul>
      <li><svg class="icon"><use href="#icon-phone"/></svg>(813) 555-0148</li>
      <li><svg class="icon"><use href="#icon-fax"/></svg>(813)</li>
      <li><svg class="icon"><use href="#icon-pin"/></svg>2386 Pennwick Dr., FL 33471-2830</li>
    </ul>
  </div>
</section>

<section class="card card-square">
  <svg class="card-bg" viewBox="0 0 720 435" preserveAspectRatio="none">
    <path d="M0 108 C150 96 380 86 470 100 C515 108 522 160 518 182 C545 150 620 112 720 104 L720 435 L0 435 Z" fill="var(--dark)"/>
    <path d="M380 90 C470 96 520 120 518 182" fill="none" stroke="var(--green-light)" stroke-width="3"/>
    <rect x="0" y="407" width="720" height="28" fill="url(#stripe)"/>
  </svg>
  <h1 class="motto">COME WHERE YOU ARE CELEBRATED!</h1>
  <p class="brand">BRIGHT MEADOW<br>ASSISTED LIVING</p>
  <div class="contact contact-left">
    <p class="name">Doris Pelling</p>
    <p class="role">Owner/Administrator</p>
    <ul>
      <li><svg class="icon"><use href="#icon-phone"/></svg>(813) 555-0148</li>
      <li><svg class="icon"><use href="#icon-fax"/></svg>(813)</li>
      <li><svg class="icon"><use href="#icon-pin"/></svg>2386 Pennwick Dr., FL 33471-2830</li>
    </ul>
  </div>
</section>

</body>
</html>
```